Quarlwick Builders Business Cards

I want to use the logo and make an unique business card that shows the textured Logo with brick and builings. I want to be able to stand out when I pass out business cards.

```html
<!DOCTYPE html>
<html lang="en">
<head>
<meta charset="UTF-8">
<title>Quarlwick Builders — Business Cards</title>
<link rel="stylesheet" href="https://fonts.googleapis.com/css2?family=Montserrat:wght@500;600;800&family=Oswald:wght@500&display=swap">
<style>
  :root {
    --page: #e9e6e1;
    --card-white: #ffffff;
    --concrete-light: #9a9a96;
    --concrete-mid: #6f6f6c;
    --concrete-dark: #3f3f3d;
    --brick-orange: #e4572e;
    --ink: #1f2a3a;
    --tagline-blue: #1d3557;
    --shadow: rgba(40, 30, 20, 0.28);
  }
  * { box-sizing: border-box; margin: 0; padding: 0; }
  html, body {
    width: 1200px; height: 902px; overflow: hidden;
    background: var(--page);
    font-family: "Montserrat", sans-serif;
  }
  .sheet {
    width: 1200px; height: 902px;
    display: flex; flex-direction: column;
    align-items: center; justify-content: center; gap: 48px;
  }
  .card {
    width: 600px; height: 343px;
    display: flex; overflow: hidden;
    box-shadow: 0 10px 24px var(--shadow);
    background: var(--card-white);
  }
  .concrete {
    background:
      radial-gradient(ellipse at 50% 45%, var(--concrete-light) 0%, var(--concrete-mid) 55%, var(--concrete-dark) 100%);
    display: flex; flex-direction: column; align-items: center; justify-content: center;
  }
  .card-front .concrete { width: 43%; }
  .card-back .concrete { width: 100%; }
  .brand {
    display: flex; align-items: center; gap: 8px;
    color: var(--brick-orange);
    font-family: "Montserrat", sans-serif; font-weight: 800;
    text-transform: uppercase; letter-spacing: 0.5px; line-height: 1.05;
    text-align: center;
  }
  .brand-mark { width: 14px; height: 14px; background: var(--brick-orange); flex: none; }
  .card-front .brand { font-size: 21px; }
  .card-back .brand { font-size: 34px; }
  .card-back .brand-mark { width: 22px; height: 22px; }
  .tagline {
    margin-top: 12px;
    font-family: "Oswald", sans-serif; font-weight: 500;
    color: var(--tagline-blue); white-space: nowrap;
  }
  .card-front .tagline { font-size: 9.5px; }
  .card-back .tagline { font-size: 15px; margin-top: 18px; }
  .details { flex: 1; padding: 50px 0 0 30px; }
  .person-name { color: var(--brick-orange); font-weight: 600; font-size: 25px; letter-spacing: 0.5px; }
  .designation {
    display: inline-block; margin-top: 4px;
    background: var(--brick-orange); color: var(--card-white);
    font-size: 12px; font-weight: 500; padding: 3px 34px 3px 12px;
    clip-path: polygon(0 0, 100% 0, 88% 100%, 0 100%);
  }
  .contact-list { list-style: none; margin-top: 36px; }
  .contact-list li {
    display: flex; align-items: flex-start; gap: 10px;
    font-size: 13px; color: var(--ink); line-height: 1.5; margin-bottom: 4px;
  }
  .contact-list svg { width: 16px; height: 16px; flex: none; margin-top: 2px; }
</style>
</head>
<body>
<main class="sheet">
  <section class="card card-front">
    <div class="concrete" role="img" aria-label="Grey concrete wall texture behind the company name">
      <div class="brand"><span class="brand-mark"></span>Quarlwick<br>Builders</div>
      <p class="tagline">Patios - Sidewalks - Retaining Walls - Foundations</p>
    </div>
    <div class="details">
      <h1 class="person-name">John Smith</h1>
      <span class="designation">Designation Here</span>
      <ul class="contact-list">
        <li>
          <svg viewBox="0 0 16 16"><circle cx="8" cy="8" r="8" fill="var(--brick-orange)"/><path d="M8 3.5a3 3 0 0 0-3 3c0 2.2 3 5.5 3 5.5s3-3.3 3-5.5a3 3 0 0 0-3-3z" fill="#fff"/></svg>
          <span>Your Address goes here,<br>Your city</span>
        </li>
        <li>
          <svg viewBox="0 0 16 16"><circle cx="8" cy="8" r="8" fill="var(--brick-orange)"/><path d="M5.5 4.5l1.5-.5 1 2-1 1a4 4 0 0 0 2 2l1-1 2 1-.5 1.5c-3 .5-6.5-3-6-6z" fill="#fff"/></svg>
          <span>0123 654 987</span>
        </li>
        <li>
          <svg viewBox="0 0 16 16"><circle cx="8" cy="8" r="8" fill="var(--brick-orange)"/><rect x="4" y="5.5" width="8" height="5" fill="#fff"/><path d="M4 5.5l4 3 4-3" stroke="var(--brick-orange)" fill="none" stroke-width="1"/></svg>
          <span>Your@email.com</span>
        </li>
        <li>
          <svg viewBox="0 0 16 16"><circle cx="8" cy="8" r="8" fill="var(--brick-orange)"/><circle cx="8" cy="8" r="4.2" stroke="#fff" fill="none"/><path d="M3.8 8h8.4M8 3.8c-2 2.5-2 5.9 0 8.4M8 3.8c2 2.5 2 5.9 0 8.4" stroke="#fff" fill="none" stroke-width=".8"/></svg>
          <span>www.QuarlwickBuilders.com</span>
        </li>
      </ul>
    </div>
  </section>

  <section class="card card-back">
    <div class="concrete" role="img" aria-label="Grey concrete wall texture behind the company name">
      <div class="brand"><span class="brand-mark"></span>Quarlwick<br>Builders</div>
      <p class="tagline">Patios - Sidewalks - Retaining Walls - Foundations</p>
    </div>
  </section>
</main>
</body>
</html>
```